TR SURFACING SPECIALISTS LTD PRESENTATION FOLDER

I need a Presentation Folder please to contain information about our services.

We are a Flooring Contractor - for information about our business please view our website: www.trsurfacing-example.co.nz

Please refer to our new brochure attached - it must fit this style and suit our brand.
Look forward to your ideas.

Also our logo needs a couple of quick changes -
Refer attached - can you please change a line and add a line -

logo
Concrete Grinding and Polishing
Resin Floors and Floor Toppings
Concrete Prep and Non Slip Coatings

Thanks Maude

Hi ALL - I just need a simple PRESENTATION FOLDER.

I already have a brochure so I don't need the same information again on my Presentation Folder.
Just something simple - with just our logo really - for ideas look at Presentation folders at Pagemill Press.
I just like the colours and style of the brochure and thought these could help you.
The presentation folder will house that brochure and other bits of information.
I hope this helps
MaudeĀ 

I just added our revised logo - and gave more specific details about what we are after - refer notes.

Thanks, MaudeĀ 

Industry/Entity Type

Business

Requirements
Must have
• I just added our updated LOGO - thought this would help match the blue.

I would like LOGO on front page with key words Quality, Value, Experience.
Plain blue inside
Back please add our guarantee, and contact details including website and email etc.

This one will come down to lay out which must match our brochure which was provided. Thank you.

```html
<!DOCTYPE html>
<html lang="en">
<head>
<meta charset="utf-8">
<title>TR Surfacing Specialists – Presentation Folder</title>
<link rel="stylesheet" href="https://fonts.googleapis.com/css2?family=Arimo:wght@400;700&display=swap">
<style>
  :root {
    --page-bg: #e9e9ea;
    --folder-blue: #6894cc;
    --swoosh-red: #e8192a;
    --swoosh-red-dark: #b0111d;
    --folder-white: #ffffff;
    --ink: #111111;
  }
  * { margin: 0; padding: 0; box-sizing: border-box; }
  html, body {
    width: 1200px;
    height: 900px;
    overflow: hidden;
    background: var(--page-bg);
    font-family: "Arimo", Arial, sans-serif;
  }
  .canvas {
    position: relative;
    width: 1200px;
    height: 900px;
  }
  .folder-front {
    position: absolute;
    left: 330px;
    top: 90px;
    width: 540px;
    height: 720px;
    background: var(--folder-white);
    box-shadow: 0 2px 10px rgba(0, 0, 0, 0.12);
    overflow: hidden;
  }
  .folder-art {
    position: absolute;
    inset: 0;
    width: 100%;
    height: 100%;
  }
  .brand-block {
    position: absolute;
    left: 328px;
    top: 590px;
    width: 140px;
    color: var(--ink);
  }
  .brand-lockup {
    display: flex;
    align-items: center;
    gap: 7px;
  }
  .brand-square {
    flex: 0 0 auto;
    width: 22px;
    height: 22px;
    background: var(--folder-blue);
  }
  .brand-name {
    font-weight: 700;
    font-size: 12px;
    line-height: 1.1;
    letter-spacing: 0.02em;
    text-transform: uppercase;
    color: var(--ink);
  }
  .service-list {
    margin-top: 6px;
    list-style: none;
    font-size: 7.4px;
    line-height: 1.25;
    text-align: center;
    color: var(--ink);
  }
</style>
</head>
<body>
  <main class="canvas">
    <section class="folder-front" aria-label="Presentation folder front cover">
      <svg class="folder-art" viewBox="0 0 540 720" preserveAspectRatio="none" aria-hidden="true">
        <path class="swoosh-red" d="M0,458 Q260,466 540,578 L540,640 Q250,478 0,466 Z" fill="var(--swoosh-red)"/>
        <path class="swoosh-shade" d="M0,458 Q260,466 540,578 L540,584 Q260,472 0,462 Z" fill="var(--swoosh-red-dark)"/>
        <path class="cover-blue" d="M0,0 H540 V578 Q260,466 0,458 Z" fill="var(--folder-blue)"/>
      </svg>

      <div class="brand-block">
        <div class="brand-lockup">
          <span class="brand-square"></span>
          <span class="brand-name">TR Surfacing<br>Specialists</span>
        </div>
        <ul class="service-list">
          <li>Concrete Grinding and Polishing</li>
          <li>Resin Floors and Floor Toppings</li>
          <li>Concrete Prep and Non Slip Coatings</li>
        </ul>
      </div>
    </section>
  </main>
</body>
</html>
```